Oversized Postcard for Estate Planning & Probate 1st 2nd and 3rd prizes

Create a professional, fresh and polished oversized post card for law firm specializing in Estate Planning & Probate Law for High Net Worth Clients

Use any picture(s) of your choice (mine or ones you recommend), logo, headshot and company info

www.morvenashbylaw.com

Westbrook Office - 4700 Kestrel Avenue, Suite 1400, Charlotte, NC 28210
Harrowgate Office - 13540 Birch Court, Suite 300, Charlotte, NC 28277

Phone (704) 555-0187

Use this card for a Free Consultation

Target Market(s)

young and old families too; business owners

Industry/Entity Type

Law Firm

Font styles to use
Serif
Sans Serif

Requirements
Must have
• Use any picture(s) of your choice (mine or ones you recommend), logo, headshot and company info
• www.morvenashbylaw.com
• Westbrook Office - 4700 Kestrel Avenue, Suite 1400, Charlotte, NC 28210
• Harrowgate Office - 13540 Birch Court, Suite 300, Charlotte, NC 28277
• Phone (704) 555-0187
• Use this card for a Free Consultation
Nice to have
• great colors and great design; like graphics with depth /shading
Should not have
• don't use too many pics - keep it simple

```html
<!DOCTYPE html>
<html lang="en">
<head>
<meta charset="utf-8">
<title>Morven Ashby Law – Oversized Postcard</title>
<link rel="stylesheet" href="https://fonts.googleapis.com/css2?family=Oswald:wght@500;600&family=Lato:ital,wght@0,400;0,700;1,400&family=Cinzel:wght@500&display=swap">
<style>
  :root{
    --blue:#0b77a6;
    --blue-deep:#0a5d85;
    --navy:#124a6a;
    --charcoal:#333539;
    --grey-light:#eeeff1;
    --grey-mid:#d9dcdf;
    --text-dark:#2f3338;
    --text-blue:#1b5f88;
    --white:#ffffff;
    --page:#d6d7d9;
  }
  *{box-sizing:border-box;margin:0;padding:0}
  html,body{width:1200px;height:1200px;overflow:hidden;background:var(--page)}
  body{position:relative;font-family:'Lato',Arial,sans-serif}
  .card{position:absolute;left:176px;width:847px;height:547px;overflow:hidden;background:var(--grey-light)}
  .card--front{top:33px}
  .card--back{top:620px;background:var(--white)}
  .card svg.shapes{position:absolute;left:0;top:0}
  .abs{position:absolute}
  .photo{position:absolute;border-radius:50%;}
  .photo--ring-grey{border:9px solid #dfe1e3;box-shadow:0 0 0 1px #c9ccd0}
  .photo--ring-navy{border:6px solid var(--white);box-shadow:0 0 0 4px var(--navy)}
  .headline{left:466px;top:38px;color:var(--white);font-family:'Oswald',Impact,sans-serif;font-weight:600;line-height:1}
  .headline__main{font-size:43px;letter-spacing:.2px}
  .headline__sub{font-size:24px;font-weight:500;margin-top:4px;transform:scaleX(.86);transform-origin:left}
  .services{left:56px;top:301px;list-style:none;font-size:14.5px;color:var(--text-dark);line-height:17.5px}
  .services li{position:relative;padding-left:16px}
  .services li::before{content:"";position:absolute;left:0;top:6px;width:7px;height:7px;border-radius:50%;background:var(--blue)}
  .call{color:var(--white);font-weight:700;font-size:17.5px;letter-spacing:.2px}
  .offices{left:53px;top:438px;font-size:13.5px;color:var(--text-dark);line-height:17px}
  .offices b{color:var(--text-blue);font-weight:700}
  .firm-mark{left:596px;top:353px;width:90px;height:70px;display:flex;justify-content:center}
  .firm-mark span{display:block;width:70px;height:70px;border-radius:50%;background:var(--blue-deep)}
  .firm-name{left:560px;top:432px;width:236px;text-align:center;font-family:'Cinzel',Georgia,serif;font-weight:500;color:var(--text-blue);line-height:1}
  .firm-name__main{font-size:26px;letter-spacing:1px}
  .firm-name__sub{font-size:11px;letter-spacing:1.5px;margin-top:3px}
  .footer-text{color:var(--white);font-style:italic;font-size:16.5px}
  .footer-text--left{left:41px;top:514px}
  .footer-text--right{left:369px;top:514px;letter-spacing:.3px}
  .intro{left:42px;top:42px;width:430px;color:var(--white);font-style:italic;font-size:12.6px;line-height:16.3px;letter-spacing:-.2px}
  .details{left:42px;top:346px;width:269px;color:var(--text-dark);font-style:italic;font-size:12.6px;line-height:16.3px;text-align:justify;letter-spacing:-.2px}
  .stamp{left:722px;top:45px;width:79px;height:79px;background:#dcdddf}
</style>
</head>
<body>

<!-- FRONT -->
<section class="card card--front">
  <svg class="shapes" width="847" height="547" viewBox="0 0 847 547">
    <defs>
      <linearGradient id="frontBlue" x1="0" y1="0" x2="1" y2="1">
        <stop offset="0" stop-color="#0a6593"/><stop offset=".6" stop-color="#0b77a6"/><stop offset="1" stop-color="#1088b8"/>
      </linearGradient>
      <linearGradient id="frontGrey" x1="0" y1="0" x2="0" y2="1">
        <stop offset="0" stop-color="#e3e5e7"/><stop offset="1" stop-color="#f4f5f6"/>
      </linearGradient>
      <linearGradient id="familyPhoto" x1="0" y1="0" x2="1" y2="1">
        <stop offset="0" stop-color="#b9d4e3"/><stop offset=".45" stop-color="#e6c4a8"/><stop offset="1" stop-color="#c98f73"/>
      </linearGradient>
    </defs>
    <rect width="847" height="547" fill="url(#frontGrey)"/>
    <polygon points="440,0 847,0 847,268 402,302" fill="url(#frontBlue)"/>
    <polygon points="428,0 440,0 402,302 390,303" fill="var(--white)"/>
    <polygon points="0,226 390,300 847,268 847,280 380,318 0,240" fill="var(--charcoal)"/>
    <polygon points="0,0 428,0 390,300 0,226" fill="url(#familyPhoto)" role="img" aria-label="Photo of a smiling three-generation family on a beach"/>
    <polygon points="0,387 318,387 298,420 0,420" fill="var(--blue)"/>
    <polygon points="0,495 340,495 310,547 0,547" fill="var(--navy)"/>
    <polygon points="340,495 354,495 324,547 310,547" fill="var(--white)"/>
    <polygon points="354,495 847,495 847,547 324,547" fill="var(--charcoal)"/>
  </svg>

  <div class="abs headline">
    <div class="headline__main">Serving clients with</div>
    <div class="headline__sub">compassion and legal guidance is our passion...</div>
  </div>

  <div class="photo photo--ring-grey" style="left:650px;top:147px;width:170px;height:170px;background:radial-gradient(circle at 50% 40%,#e9c79c,#c0864f 70%,#9a6238)" role="img" aria-label="Photo of a young father with two children"></div>
  <div class="photo photo--ring-grey" style="left:450px;top:148px;width:218px;height:218px;background:radial-gradient(circle at 50% 45%,#e2c3a3,#b97a45 65%,#7c5230)" role="img" aria-label="Photo of a smiling senior couple outdoors in autumn"></div>

  <ul class="abs services">
    <li>Estate Administration</li>
    <li>Probate Law, Estate Planning</li>
    <li>Wills, Trusts, Living Wills</li>
    <li>Healthcare Powers</li>
  </ul>

  <div class="abs call" style="left:55px;top:393px">CALL US AT:&nbsp; (704) 555-0187</div>

  <div class="abs offices">
    <div><b>Westbrook Office</b> - 4700 Kestrel Avenue, Suite 1400, Charlotte, NC 28210</div>
    <div><b>Harrowgate Office</b> - 13540 Birch Court, Suite 300, Charlotte, NC 28277</div>
  </div>

  <div class="abs firm-mark"><span></span></div>
  <div class="abs firm-name">
    <div class="firm-name__main">MORVEN ASHBY</div>
    <div class="firm-name__sub">LAW, PLLC</div>
  </div>

  <div class="abs footer-text footer-text--left">Use this card for a Free Consultation</div>
  <div class="abs footer-text footer-text--right">Please visit us to know more at: www.morvenashbylaw.com</div>
</section>

<!-- BACK -->
<section class="card card--back">
  <svg class="shapes" width="847" height="547" viewBox="0 0 847 547">
    <defs>
      <linearGradient id="backBlue" x1="0" y1="0" x2="1" y2="1">
        <stop offset="0" stop-color="#0a6593"/><stop offset=".7" stop-color="#0b77a6"/><stop offset="1" stop-color="#0d82b4"/>
      </linearGradient>
      <linearGradient id="backGrey" x1="0" y1="0" x2="0" y2="1">
        <stop offset="0" stop-color="#e1e3e5"/><stop offset="1" stop-color="#f2f3f4"/>
      </linearGradient>
    </defs>
    <polygon points="0,0 600,0 470,250 0,128" fill="url(#backBlue)"/>
    <polygon points="610,0 629,0 553,126 535,126" fill="var(--navy)"/>
    <polygon points="0,122 440,245 434,262 0,140" fill="var(--white)"/>
    <polygon points="0,128 440,248 0,135" fill="var(--navy)"/>
    <polygon points="0,140 434,262 370,493 0,493" fill="url(#backGrey)"/>
    <polygon points="0,265 325,265 305,300 0,300" fill="var(--blue)"/>
    <polygon points="0,493 340,493 310,547 0,547" fill="var(--navy)"/>
    <polygon points="340,493 354,493 324,547 310,547" fill="var(--white)"/>
    <polygon points="354,493 847,493 847,547 324,547" fill="var(--charcoal)"/>
  </svg>

  <p class="abs intro">The Charlotte law firm of Morven Ashby Law, PLLC focuses on serving clients in the areas of: estate planning, estate administration, probate law, special needs planning, succession planning and general business law. Morven Ashby Law, PLLC is conveniently located in the Westbrook Towers in Charlotte, NC.</p>

  <div class="photo photo--ring-navy" style="left:424px;top:117px;width:150px;height:150px;background:radial-gradient(circle at 60% 30%,#f3d9b4,#c8935f 60%,#7d5637)" role="img" aria-label="Photo of two small children sitting together looking at the sunset"></div>
  <div class="photo photo--ring-navy" style="left:334px;top:246px;width:210px;height:210px;background:radial-gradient(circle at 50% 50%,#f4f1ec,#d9d1c6 65%,#b8ab9b)" role="img" aria-label="Photo of a child playing pilot with a toy airplane"></div>

  <div class="abs stamp" role="img" aria-label="Postage stamp area"></div>

  <div class="abs call" style="left:43px;top:271px">CALL US AT:&nbsp; (704) 555-0187</div>

  <p class="abs details">Morven Ashby Law, PLLC serving clients in estate planning, estate administration, probate law, wills, revocable trusts, irrevocable trusts, powers of attorney, health care powers of attorney, living wills, hipaa releases, guardianships, special needs planning, wealth transfers, elder law &amp; business law in North Carolina and South Carolina.</p>

  <div class="abs footer-text footer-text--left" style="top:512px">Use this card for a Free Consultation</div>
  <div class="abs footer-text footer-text--right" style="top:512px">Please visit us to know more at: www.morvenashbylaw.com</div>
</section>

</body>
</html>
```